TB - WESITE NEEDED PAGE: Clean / Modern / Pro & Dynamic

Tavlin-Brokers is a new insurance brokerage firm dealing exclusively with companies (BToB) providing the following property: Liabilities Insurance Insurances Automobile Insurance Insurances Construction% 26amp; Engineering Casualty Workmen 's Compensation Health Insurance Marime% 26amp; Transit Credit Insurance Young, Fast, Proactive and Dynamic we call ourselves Tavlin-Brokers because we are a "start-up" willing to make a difference in the market, bringing modernity and speed to our industry, still too bureaucratic / procedural / opaque uninitiated. We need something respecting the colors of our orange logtype; blue; white; black; easy to scroll, with simple information on the company; - who we are - our team (with the pictures) - what we do - what we do - contact us, contact us (google map) Luanda (Angola) Small company, just need something flashy / professional / structured / modern.

Target Market(s)

BtoB; Oil and gas companies; French speaking copying established in Angola, all industrials, factories and importers of goods.

Industry/Entity Type

Insurance Broker

Font styles to use
Sans Serif

Colors

Designer to choose colors to be used in the design.

Requirements
Must have
• We need something respecting the colors of our orange logtype; blue; white; black; easy to scroll, with simple information on the company; - who we are - our team (with the pictures) - what we do - what we do - contact us, contact us (google map) Luanda (Angola) Small company, just need something flashy / professional / structured / modern.
Nice to have
• A page format
Should not have
• WE DO NOT WANT A REFER TO OUR LOGO, but a Home Page for our Website with the basics categories ... >> PLEASE CAREFULLY USE THE RIGHT COLOR OF THE LOGOTYPE which are the ones enclosed Orange / Turquoise / Black as per the business card .

```html
<!DOCTYPE html>
<html lang="en">
<head>
<meta charset="utf-8">
<title>Tavlin-Brokers — Insurance Brokerage</title>
<link href="https://fonts.googleapis.com/css2?family=Montserrat:wght@300;400;500;600;700;800&family=Lato:wght@400;700&display=swap" rel="stylesheet">
<style>
:root{
  --orange:#f26522;
  --orange-dark:#c4470f;
  --blue:#1a9ad6;
  --ink:#1c1c1c;
  --text:#5b5b5b;
  --muted:#8a8f99;
  --rule:#ececec;
  --light:#f6f6f6;
  --white:#ffffff;
}
*{box-sizing:border-box;margin:0;padding:0}
html,body{width:1200px;height:3075px;overflow:hidden}
body{position:relative;background:var(--white);font-family:"Lato",sans-serif;color:var(--text)}
.abs{position:absolute}
.display{font-family:"Montserrat",sans-serif;color:var(--ink)}

/* Hero */
.hero{left:0;top:0;width:1200px;height:583px;background:linear-gradient(180deg,#2b2d31 0%,#45484d 45%,#6d6f72 80%,#8c8d8f 100%)}
.brand{display:flex;align-items:center;gap:10px;font-family:"Montserrat",sans-serif;font-weight:700;font-size:17px;color:var(--orange);letter-spacing:.2px}
.brand-dot{width:34px;height:34px;border-radius:50%;background:var(--orange)}
.main-nav{right:161px;top:40px;display:flex;gap:31px}
.main-nav a{font-family:"Montserrat",sans-serif;font-size:12px;color:#fff;text-decoration:none;letter-spacing:.2px}
.hero-title{top:240px;text-align:center;color:#fff;font-family:"Montserrat",sans-serif}
.hero-title .l1{display:block;font-weight:800;font-size:39px;letter-spacing:1.5px}
.hero-title .l2{display:block;font-weight:400;font-size:32px;margin-top:6px;letter-spacing:.5px}
.btn{background:var(--orange);color:#fff;font-family:"Montserrat",sans-serif;font-weight:600;font-size:11px;display:flex;align-items:center;justify-content:center}
.hero-btn{left:426px;top:347px;width:144px;height:41px}

/* Guides */
.guide{top:583px;width:1px;height:1136px;background:var(--rule)}

.kicker{font-family:"Montserrat",sans-serif;font-weight:600;font-size:13px;color:var(--muted)}
.h2{font-family:"Montserrat",sans-serif;font-weight:400;font-size:38px;color:var(--ink);line-height:1.15}
.h2 b{font-weight:800}
.body-copy{font-size:13px;line-height:19.5px;color:var(--text)}
.more{font-family:"Montserrat",sans-serif;font-weight:600;font-size:12px;color:var(--blue);border-bottom:1px solid var(--blue);padding-bottom:1px}

/* About */
.since{left:161px;top:700px;font-family:"Montserrat",sans-serif;font-weight:600;font-size:12px;color:var(--ink)}
.about-photo{left:161px;top:730px;width:300px;height:413px;background:linear-gradient(135deg,#dfe6ec 0%,#b9c7d3 55%,#9aa7b3 100%)}
.about-frame{left:461px;top:814px;width:70px;height:222px;border:4px solid var(--orange);border-left:none}

/* Services */
.service{width:270px}
.service h3{font-family:"Montserrat",sans-serif;font-weight:700;font-size:13.5px;color:var(--ink);margin:22px 0 14px}
.service p{margin-bottom:28px}

/* Gallery */
.tile{top:1719px;height:279px}
.tag{top:1858px;height:23px;padding:0 8px;background:var(--orange);color:#fff;font-family:"Montserrat",sans-serif;font-weight:600;font-size:12px;display:flex;align-items:center}
.arrow{top:1840px}

/* Team */
.team{left:0;top:1998px;width:1200px;height:481px;background-color:#f7f7f7;background-image:radial-gradient(#e4e4e4 1px,transparent 1px);background-size:6px 6px}
.member{top:2137px;width:172px;text-align:center}
.member .photo{width:172px;height:227px;background:linear-gradient(180deg,#f2f2f2 0%,#c9ccd1 60%,#2f3440 100%)}
.member .name{font-family:"Montserrat",sans-serif;font-weight:500;font-size:17px;color:var(--muted);margin-top:16px}
.member .role{font-family:"Montserrat",sans-serif;font-weight:600;font-size:10px;color:var(--ink);margin-top:8px}

/* Map */
.map{left:0;top:2479px;width:1200px;height:286px;background:linear-gradient(135deg,#e9e9e9,#dcdcdc)}
.map-pin-label{left:475px;top:2566px;display:flex;align-items:center;gap:6px;font-family:"Montserrat",sans-serif;font-weight:600;font-size:12px;color:#333}
.map-card{left:498px;top:2606px;width:272px;height:58px;background:#fff;box-shadow:0 1px 3px rgba(0,0,0,.2);display:flex;gap:8px;padding:10px 12px;font-size:11px;line-height:16px;color:#333}

/* Footer */
.foot-about{left:161px;top:2906px;width:270px;font-size:11.5px;line-height:17px}
.foot-h{font-family:"Montserrat",sans-serif;font-weight:700;font-size:12.5px;color:var(--ink)}
.foot-list{list-style:none;font-size:11.5px;color:var(--text)}
.foot-list li{line-height:25px}
.contact-row{display:flex;gap:10px;font-size:11.5px;line-height:17px;margin-bottom:10px}
.rule{left:161px;top:3023px;width:875px;height:1px;background:var(--rule)}
.copyright{left:161px;top:3044px;font-size:11px;color:var(--muted)}
.copyright b{color:var(--ink);font-weight:400}
.social{right:162px;top:3044px;display:flex;gap:18px}
.social span{width:11px;height:11px;border-radius:50%;background:var(--ink)}
</style>
</head>
<body>

<!-- Hero -->
<section class="abs hero" role="img" aria-label="Businessman sketching a house outline over a city skyline, with a home, family and car silhouette"></section>
<div class="abs brand" style="left:161px;top:40px"><span class="brand-dot"></span>TAVLIN-BROKERS</div>
<nav class="abs main-nav">
  <a href="#">HOME</a><a href="#">ABOUT US</a><a href="#">WHO WE ARE</a><a href="#">OUR TEAM</a><a href="#">WHAT WE DO</a><a href="#">CONTACT US</a>
</nav>
<h1 class="abs hero-title" style="left:0;width:998px"><span class="l1">BE LIFE CONFIDENT.</span><span class="l2">GO AHEAD WITH TAVLIN BROKERS.</span></h1>
<a class="abs btn hero-btn">CONTACT US</a>

<!-- Column guides -->
<div class="abs guide" style="left:161px"></div>
<div class="abs guide" style="left:460px"></div>
<div class="abs guide" style="left:758px"></div>
<div class="abs guide" style="left:1036px"></div>

<!-- Who we are -->
<div class="abs since">SINCE 2014</div>
<div class="abs about-photo" role="img" aria-label="Smiling broker in shirt and tie holding out a clipboard"></div>
<div class="abs about-frame"></div>

<div class="abs kicker" style="left:615px;top:730px">Who We Are</div>
<h2 class="abs h2" style="left:615px;top:756px">WHO <b>TAVLIN<br>BROKERS</b> ARE</h2>
<div class="abs body-copy" style="left:615px;top:872px;width:420px">
  <p>Lorem ipsum dolor sit amet, consectetur adipiscing elit, sed do eiusmod tempor incididunt ut labore et dolore magna aliqua. Ut enim ad minim veniam, quis nostrud exercitation ullamco laboris nisi ut aliquip ex ea commodo consequat.</p>
  <p style="margin-top:24px">Ut enim ad minim veniam, quis nostrud exercitation ullamco laboris nisi ut aliquip ex ea commodo consequat. Lorem ipsum dolor sit amet, consectetur adipiscing elit, sed do eiusmod tempor incididunt ut labore et dolore magna aliqua.</p>
</div>
<a class="abs more" style="left:615px;top:1096px">READ MORE</a>

<!-- What we do -->
<div class="abs kicker" style="left:161px;top:1231px">What We Do</div>
<h2 class="abs h2" style="left:161px;top:1255px">WHAT <b>TAVLIN BROKERS</b> DO</h2>

<div class="abs service" style="left:161px;top:1331px">
  <svg width="58" height="56" viewBox="0 0 58 56" fill="none" stroke="#1c1c1c" stroke-width="2"><rect x="3" y="20" width="22" height="34"/><rect x="25" y="4" width="16" height="50"/><rect x="41" y="26" width="14" height="28"/><path d="M8 26h4M16 26h4M8 34h4M16 34h4M8 42h4M16 42h4M30 12h6M30 20h6M30 28h6M30 36h6M30 44h6M45 34h6M45 42h6"/></svg>
  <h3>LIABILITIES INSURANCE</h3>
  <p class="body-copy">Lorem ipsum dolor sit amet, consectetur adipiscing elit, sed do eiusmod tempor incididunt ut labore et dolore magna aliqua.</p>
  <a class="more">READ MORE</a>
</div>
<div class="abs service" style="left:460px;top:1331px">
  <svg width="66" height="56" viewBox="0 0 66 56"><path d="M12 22 L18 6 H48 L54 22 H60 V46 H54 V54 H44 V46 H22 V54 H12 V46 H6 V22 Z" fill="#1c1c1c"/><path d="M18 22 L22 11 H44 L48 22 Z" fill="#fff"/><circle cx="16" cy="34" r="4" fill="#fff"/><circle cx="50" cy="34" r="4" fill="#fff"/></svg>
  <h3>AUTOMOBILE INSURANCE</h3>
  <p class="body-copy">Lorem ipsum dolor sit amet, consectetur adipiscing elit, sed do eiusmod tempor incididunt ut labore et dolore magna aliqua.</p>
  <a class="more">READ MORE</a>
</div>
<div class="abs service" style="left:758px;top:1331px">
  <svg width="58" height="56" viewBox="0 0 58 56" fill="none" stroke="#1c1c1c" stroke-width="2"><rect x="3" y="18" width="26" height="36"/><path d="M9 24h5M18 24h5M9 32h5M18 32h5M9 40h5M18 40h5M9 48h5M18 48h5"/><path d="M34 10 L46 4 L50 12 L44 16 Z"/><path d="M46 14 V46 M40 46 h14 v8 h-14 z"/></svg>
  <h3>CONSTRUCTION INSURANCE</h3>
  <p class="body-copy">Lorem ipsum dolor sit amet, consectetur adipiscing elit, sed do eiusmod tempor incididunt ut labore et dolore magna aliqua.</p>
  <a class="more">READ MORE</a>
</div>

<!-- We work with -->
<h2 class="abs display" style="left:161px;top:1646px;font-weight:800;font-size:38px;letter-spacing:1px">WE WORK WITH</h2>
<div class="abs tile" style="left:0;width:297px;background:linear-gradient(160deg,#6e879c,#3c5a4e 70%,#2c3b33)" role="img" aria-label="Container ship at a port"></div>
<div class="abs tile" style="left:301px;width:297px;background:linear-gradient(160deg,#5b5a3a,#b69f2a 55%,#3d3c2c)" role="img" aria-label="Industrial worker in hard hat and hi-vis jacket"></div>
<div class="abs tile" style="left:602px;width:297px;background:linear-gradient(160deg,#d9dde2,#9ea4ab 55%,#b3262b)" role="img" aria-label="Car salesman with clipboard beside a red car"></div>
<div class="abs tile" style="left:903px;width:297px;background:linear-gradient(160deg,#e6e4df,#c8c4bd 60%,#8e8b86)" role="img" aria-label="Engineer in yellow hard hat on a construction site"></div>
<div class="abs tag" style="left:197px">OIL COMPANY</div>
<div class="abs tag" style="left:302px">INDUSTRIES</div>
<div class="abs tag" style="left:800px">AUTOMOBILE</div>
<div class="abs tag" style="left:903px">CONSTRUCTION</div>
<svg class="abs arrow" style="left:42px" width="24" height="40" viewBox="0 0 24 40"><path d="M20 2 L4 20 L20 38" fill="none" stroke="#fff" stroke-width="2.5"/></svg>
<svg class="abs arrow" style="left:1132px" width="24" height="40" viewBox="0 0 24 40"><path d="M4 2 L20 20 L4 38" fill="none" stroke="#fff" stroke-width="2.5"/></svg>

<!-- Team -->
<section class="abs team"></section>
<div class="abs kicker" style="left:161px;top:2051px">Our Team</div>
<h2 class="abs h2" style="left:161px;top:2076px">OUR <b>TEAM</b></h2>
<div class="abs member" style="left:160px"><div class="photo" role="img" aria-label="Team member portrait in dark suit"></div><div class="name">John Smith</div><div class="role">MEMBERS</div></div>
<div class="abs member" style="left:395px"><div class="photo" role="img" aria-label="Team member portrait in light shirt"></div><div class="name">John Smith</div><div class="role">MEMBERS</div></div>
<div class="abs member" style="left:630px"><div class="photo" role="img" aria-label="Team member portrait in navy suit"></div><div class="name">John Smith</div><div class="role">MEMBERS</div></div>
<div class="abs member" style="left:865px"><div class="photo" role="img" aria-label="Team member portrait in blue blazer"></div><div class="name">John Smith</div><div class="role">MEMBERS</div></div>

<!-- Map -->
<section class="abs map" role="img" aria-label="Street map showing the office location"></section>
<div class="abs map-pin-label">
  <svg width="12" height="16" viewBox="0 0 12 16"><path d="M6 1a5 5 0 0 0-5 5c0 4 5 9 5 9s5-5 5-9a5 5 0 0 0-5-5z" fill="none" stroke="#333" stroke-width="1.6"/><circle cx="6" cy="6" r="1.8" fill="#333"/></svg>
  Shop Name
</div>
<div class="abs map-card">
  <svg width="14" height="18" viewBox="0 0 12 16" style="flex:none"><path d="M6 1a5 5 0 0 0-5 5c0 4 5 9 5 9s5-5 5-9a5 5 0 0 0-5-5z" fill="none" stroke="var(--orange)" stroke-width="1.8"/><circle cx="6" cy="6" r="1.8" fill="var(--orange)"/></svg>
  <div>Lorem Ipsum Dolor Sit Amet Conse<br>ctetor Dolor Sit Amet Lorem Ipsum Dolor.</div>
</div>

<!-- Footer -->
<div class="abs brand" style="left:161px;top:2858px"><span class="brand-dot"></span>TAVLIN-BROKERS</div>
<p class="abs foot-about">Ut enim ad minim veniam, quis nostrud exercitation ullamco laboris nisi ut aliquip ex ea commodo consequat. Lorem ipsum dolor sit amet, consectetur adipiscing elit, sed do eiusmod</p>

<div class="abs" style="left:538px;top:2830px;width:300px">
  <div class="foot-h" style="margin-bottom:12px">Contact Us</div>
  <div class="contact-row"><svg width="12" height="17" viewBox="0 0 12 16" style="flex:none"><path d="M6 1a5 5 0 0 0-5 5c0 4 5 9 5 9s5-5 5-9a5 5 0 0 0-5-5z" fill="none" stroke="#333" stroke-width="1.6"/><circle cx="6" cy="6" r="1.8" fill="#333"/></svg><span>Lorem Ipsum Dolor Sit Amet<br>Consectetor Dolor Sit Amet Lorem Ipsum Dolor.</span></div>
  <div class="contact-row"><svg width="12" height="12" viewBox="0 0 12 12" style="flex:none;margin-top:3px"><path d="M3 1 L5 4 L4 5.5 C5 7.5 6 8.5 7 9 L8.5 8 L11 10 L9.5 11.5 C5 11 1 7 0.5 2.5 Z" fill="#333"/></svg><span>+244 923 480 157</span></div>
  <div class="contact-row"><svg width="13" height="10" viewBox="0 0 13 10" style="flex:none;margin-top:4px"><rect x="0.7" y="0.7" width="11.6" height="8.6" fill="none" stroke="#333" stroke-width="1.2"/><path d="M1 1 L6.5 5.5 L12 1" fill="none" stroke="#333" stroke-width="1.2"/></svg><span>info@tavlinbrokers.com</span></div>
</div>

<div class="abs" style="left:900px;top:2830px">
  <div class="foot-h" style="margin-bottom:4px">Navigations</div>
  <ul class="foot-list">
    <li>-&nbsp; Home</li><li>-&nbsp; Who We Are</li><li>-&nbsp; What We Do</li><li>-&nbsp; Our team</li><li>-&nbsp; Contact Us</li>
  </ul>
</div>

<div class="abs rule"></div>
<div class="abs copyright">© Copyright 2019 <b>Tavlin Brokers</b>, All Rights Reserved.</div>
<div class="abs social"><span></span><span></span><span></span><span></span></div>

</body>
</html>
```